Wine Label Redesign For California Wine Company

We’re looking to refresh our brand with a new professional looking label. We love what we have and was well received over the past three years and would like to keep a couple of the element: Name (Hugo Brantley), it doesn’t have to be in cursive. The swirl, this how everybody recognizes our brand as it’s also in our logo. Colors: Gold and whatever you think is awesome. Looking forward to seeing your work.

Target Market(s)

Retailers

Industry/Entity Type

Winery

Font styles to use
Serif
Script

Colors

Designer to choose colors to be used in the design.

Requirements
Must have
• Front Label:
• Symphony (Varietal)
• 2016 (vintage)
• Lodi, California (location)
• Hugo Brantley (Name)
• Back Label:
• Government Warning
• www.brantleywineco.com (website)
• 2016 (vintage)
• Swirl
Nice to have
• Creativity
• Bold colors
• Something that pops
Should not have
• Should not look nothing like my old label.

```html
<!DOCTYPE html>
<html lang="en">
<head>
<meta charset="utf-8">
<title>Symphony – Hugo Brantley Wine Labels</title>
<link rel="stylesheet" href="https://fonts.googleapis.com/css2?family=Cinzel:wght@400;600&family=Alegreya:wght@500;700&family=EB+Garamond:wght@400;700&family=Courgette&display=swap">
<style>
  :root {
    --backdrop: #c1b8b1;
    --label-black: #050505;
    --gold: #d4b04a;
    --gold-deep: #a8842a;
    --cream-light: #fbf8f0;
    --cream-mid: #eee4d2;
    --cream-edge: #ddd0b8;
    --ink: #111111;
    --year-white: #e8e4dc;
  }
  * { box-sizing: border-box; margin: 0; padding: 0; }
  html, body { width: 986px; height: 1200px; overflow: hidden; }
  body {
    background: var(--backdrop);
    position: relative;
  }
  .label {
    position: absolute;
    top: 393px;
    width: 414px;
    height: 414px;
    background: var(--label-black);
    overflow: hidden;
  }
  .label--front { left: 62px; }
  .label--back { left: 511px; }

  .varietal-band {
    position: absolute; left: 0; top: 0; width: 100%; height: 63px;
    display: flex; align-items: center; justify-content: center;
  }
  .varietal {
    font-family: "Cinzel", serif;
    font-weight: 400;
    font-size: 28px;
    letter-spacing: 9px;
    color: var(--gold);
    padding-left: 9px;
  }
  .gold-rule {
    position: absolute; left: 0; width: 100%; height: 1.5px;
    background: linear-gradient(90deg, var(--gold-deep), var(--gold), var(--gold-deep));
  }
  .gold-rule--top { top: 63px; }
  .gold-rule--bottom { top: 328px; }

  .panel {
    position: absolute; left: 0; top: 66px; width: 100%; height: 260px;
    overflow: hidden;
    background: radial-gradient(ellipse at 45% 40%, var(--cream-light) 0%, var(--cream-mid) 60%, var(--cream-edge) 100%);
  }

  .origin-band {
    position: absolute; left: 0; top: 331px; width: 100%; height: 83px;
    display: flex; flex-direction: column; align-items: center; justify-content: center;
  }
  .origin {
    font-family: "Alegreya", serif;
    font-weight: 700;
    font-size: 19px;
    letter-spacing: 2.5px;
    color: var(--gold);
    padding: 3px 4px 4px;
    border-top: 1px solid var(--gold-deep);
    border-bottom: 1px solid var(--gold-deep);
  }
  .vintage {
    margin-top: 7px;
    font-family: "EB Garamond", serif;
    font-size: 11px;
    letter-spacing: 7px;
    color: var(--year-white);
    padding-left: 7px;
  }

  /* front */
  .producer-vertical {
    position: absolute;
    left: 112px; top: 128px;
    transform: translate(-50%, -50%) rotate(-90deg);
    font-family: "Courgette", cursive;
    font-size: 32px;
    line-height: 1;
    color: var(--ink);
    white-space: nowrap;
  }
  .brand-mark {
    position: absolute; left: 170px; top: 35px; width: 200px; height: 190px;
    display: flex; flex-direction: column; align-items: center; justify-content: center; gap: 12px;
  }
  .brand-mark__dot {
    width: 70px; height: 70px; border-radius: 50%;
    background: var(--gold);
  }
  .brand-mark__name {
    font-family: "Cinzel", serif;
    font-weight: 600;
    font-size: 17px;
    letter-spacing: 2px;
    color: var(--gold-deep);
  }

  /* back */
  .producer-line {
    position: absolute; left: 0; top: 36px; width: 100%;
    display: flex; align-items: center; justify-content: center; gap: 14px;
  }
  .producer-line__name {
    font-family: "Courgette", cursive;
    font-size: 27px;
    line-height: 1.2;
    color: var(--ink);
  }
  .producer-line__dot {
    width: 30px; height: 30px; border-radius: 50%;
    background: var(--gold);
  }
  .warning {
    position: absolute; left: 58px; top: 98px; width: 298px;
    font-family: "EB Garamond", serif;
    font-size: 10.6px;
    line-height: 12.3px;
    text-transform: uppercase;
    text-align: justify;
    color: var(--ink);
  }
  .warning strong { font-weight: 700; }
  .facts {
    position: absolute; left: 57px; top: 197px; width: 300px;
    border: 1px solid var(--ink);
  }
  .facts__row {
    height: 23px;
    display: flex; align-items: center; justify-content: center; gap: 6px;
    font-family: "EB Garamond", serif;
    font-weight: 700;
    font-size: 10px;
    color: var(--ink);
    background: var(--cream-light);
  }
  .facts__web {
    height: 24px;
    display: flex; align-items: center; justify-content: center;
    background: var(--label-black);
    font-family: "EB Garamond", serif;
    font-weight: 700;
    font-size: 10px;
    letter-spacing: 2.5px;
    text-transform: uppercase;
    color: var(--gold);
  }
</style>
</head>
<body>

<section class="label label--front">
  <div class="varietal-band"><span class="varietal">SYMPHONY</span></div>
  <div class="gold-rule gold-rule--top"></div>
  <div class="panel" role="img" aria-label="Cream panel with faint damask pattern">
    <div class="producer-vertical">Hugo Brantley</div>
    <div class="brand-mark">
      <div class="brand-mark__dot"></div>
      <div class="brand-mark__name">Hugo Brantley</div>
    </div>
  </div>
  <div class="gold-rule gold-rule--bottom"></div>
  <div class="origin-band">
    <span class="origin">Lodi, California</span>
    <span class="vintage">2016</span>
  </div>
</section>

<section class="label label--back">
  <div class="varietal-band"><span class="varietal">SYMPHONY</span></div>
  <div class="gold-rule gold-rule--top"></div>
  <div class="panel" role="img" aria-label="Cream panel with faint damask pattern">
    <div class="producer-line">
      <span class="producer-line__name">Hugo Brantley</span>
      <span class="producer-line__dot"></span>
    </div>
    <p class="warning"><strong>Government warning:</strong> (1) According to the Surgeon General, women should not drink alcoholic beverages during pregnancy because of the risk of birth defects. (2) Consumption of alcoholic beverages impairs your ability to drive a car or operate machinery, and may cause health problems.</p>
    <div class="facts">
      <div class="facts__row"><span>CONTAINS SULFITES</span><span>|</span><span>ALC 14.2% BY VOL</span><span>|</span><span>750ML</span></div>
      <div class="facts__web">www.brantleywineco.com</div>
    </div>
  </div>
  <div class="gold-rule gold-rule--bottom"></div>
  <div class="origin-band">
    <span class="origin">Lodi, California</span>
    <span class="vintage">2016</span>
  </div>
</section>

</body>
</html>
```